Flyer for American Indian Elders on Dementia Warning Signs

We need a flyer designed for older adults who are American Indian or Alaska Native (in the U.S.).

Ideally, the flyer should complement the colors of our logos. The project logo and our organization logo are attached to the brief.

When people see the flyer we want them to feel that it represents their culture, is warm, and professional but relatable to older adults and people who have limited incomes.

I have attached an earlier draft of the document we designed ourselves BUT we want different and better.

It is for older adults who have trouble reading so:
1. you must use a font that is 11.5 points or larger
2. Do not put text over complex pictures or use shading with words
3. You can use a serif font for the heading, but should use san serif for the body text
4. There should be good contrast between the font color and background

Please do not use any images that include a head dress or pictures of American Indian people or things that are very traditional or "token" imagery.

We need to save a small space under the call out box/ somewhere on the flyer for other people to add their logo once they download.

Let us know if you have questions or need additional information.

Target Market(s)

Older American Indian people

Font styles to use
Serif
Sans Serif

Requirements
Must have
• Easy to read for older adults
Should not have
• indian headdress

```html
<!DOCTYPE html>
<html lang="en">
<head>
<meta charset="utf-8">
<title>10 Signs of Thinking or Memory Changes That Might Be Dementia</title>
<link rel="stylesheet" href="https://fonts.googleapis.com/css2?family=Poppins:ital,wght@0,300;0,400;0,500;0,600;0,700;1,300;1,400&display=swap">
<style>
  :root {
    --teal: #28afc9;
    --mauve: #b5716a;
    --white: #ffffff;
    --ink: #1f1f1f;
    --photo-light: #f2eee9;
    --photo-mid: #b89a86;
    --photo-dark: #3a2f2a;
  }
  * { box-sizing: border-box; margin: 0; padding: 0; }
  html, body { width: 927px; height: 1200px; overflow: hidden; background: var(--white); }
  .flyer {
    position: relative;
    width: 927px;
    height: 1200px;
    overflow: hidden;
    background: var(--white);
    font-family: "Poppins", sans-serif;
    color: var(--ink);
  }
  .title-band {
    position: absolute; left: 0; top: 0; width: 927px; height: 142px;
    background: var(--teal);
  }
  .title {
    position: absolute; left: 0; top: 20px; width: 927px;
    text-align: center; color: var(--white);
    font-weight: 600; font-size: 37px; line-height: 46px; letter-spacing: -0.3px;
  }
  .accent-band {
    position: absolute; left: 0; top: 142px; width: 927px; height: 12px;
    background: var(--mauve);
  }
  .photo {
    position: absolute; left: 160px; top: 154px; width: 570px; height: 386px;
    background:
      radial-gradient(ellipse 200px 180px at 470px 230px, var(--photo-mid) 0%, rgba(184,154,134,0.6) 55%, rgba(255,255,255,0) 100%),
      radial-gradient(ellipse 260px 200px at 200px 90px, var(--photo-dark) 0%, rgba(58,47,42,0.45) 50%, rgba(255,255,255,0) 100%),
      var(--white);
  }
  .intro-panel { position: absolute; left: 0; top: 178px; width: 332px; height: 139px; }
  .intro-panel p {
    position: absolute; left: 28px; top: 20px; width: 235px;
    color: var(--white); font-size: 11.6px; line-height: 14.6px; font-weight: 400;
  }
  .org-card {
    position: absolute; left: 658px; top: 118px; width: 230px; height: 202px;
    background: var(--white);
    box-shadow: 4px 4px 8px rgba(0,0,0,0.35);
  }
  .org-card .mark {
    position: absolute; left: 93px; top: 40px; width: 44px; height: 44px;
    background: var(--teal);
  }
  .org-card .org-name {
    position: absolute; left: 18px; top: 104px; width: 194px;
    text-align: center; color: var(--teal);
    font-weight: 600; font-size: 17px; line-height: 21px;
  }
  .signs { position: absolute; left: 28px; width: 490px; font-size: 11.6px; line-height: 14.55px; }
  .signs .lead { font-weight: 500; }
  .signs .note { font-style: italic; font-weight: 300; }
  .signs ul { list-style: none; }
  .signs li { font-style: italic; font-weight: 300; }
  .signs li::before { content: "\2022\00a0"; font-style: normal; }
  .intro { font-weight: 300; width: 330px; }
  .callout-frame {
    position: absolute; left: 542px; top: 606px; width: 385px; height: 437px;
    background: var(--teal);
  }
  .callout {
    position: absolute; left: 556px; top: 618px; width: 335px; height: 413px;
    background: var(--white); padding: 22px 10px 0 20px;
  }
  .callout p {
    font-weight: 600; font-size: 18px; line-height: 21.8px; margin-bottom: 22px;
  }
  .callout p::before {
    content: ""; display: inline-block; width: 9px; height: 9px; margin-right: 6px;
    vertical-align: 2px;
  }
  .callout .teal { color: var(--teal); }
  .callout .teal::before { background: var(--mauve); }
  .callout .mauve { color: var(--mauve); }
  .callout .mauve::before { background: var(--teal); }
  .footer-band {
    position: absolute; left: 0; top: 1043px; width: 927px; height: 157px;
    background: var(--teal);
  }
  .partner-card {
    position: absolute; left: 28px; top: 1072px; width: 314px; height: 97px;
    background: var(--white);
  }
  .partner-card .mark {
    position: absolute; left: 14px; top: 18px; width: 60px; height: 60px;
    border-radius: 50%; background: var(--teal);
  }
  .partner-card .partner-name {
    position: absolute; left: 88px; top: 20px; width: 215px;
    color: var(--teal); font-weight: 600; font-size: 16px; line-height: 19px;
  }
  .project-card {
    position: absolute; left: 356px; top: 1027px; width: 186px; height: 158px;
    background: var(--white);
  }
  .project-card .mark {
    position: absolute; left: 75px; top: 38px; width: 36px; height: 36px;
    background: var(--mauve);
  }
  .project-card .project-name {
    position: absolute; left: 0; top: 112px; width: 186px; text-align: center;
    color: var(--teal); font-weight: 600; font-size: 12px; line-height: 14px;
  }
  .learn-more {
    position: absolute; left: 576px; top: 1063px; width: 340px;
    color: var(--white); font-size: 17.5px; line-height: 21.8px; font-weight: 400;
  }
</style>
</head>
<body>
<main class="flyer">
  <div class="title-band"></div>
  <h1 class="title">10 SIGNS OF THINKING OR MEMORY CHANGES<br>THAT MIGHT BE DEMENTIA</h1>
  <div class="accent-band"></div>

  <div class="photo" role="img" aria-label="Photo of an older woman seated indoors near a window with blinds, faded softly into the white page"></div>

  <div class="intro-panel">
    <svg width="332" height="139" viewBox="0 0 332 139" aria-hidden="true">
      <polygon points="0,0 200,0 332,139 0,139" fill="var(--mauve)"/>
    </svg>
    <p>As we get older, we may slow down a bit. This is a normal part of aging. Changes in memory or thinking that make it harder to get through the day, are not a normal part of aging. These may be early signs of dementia.</p>
  </div>

  <div class="org-card">
    <div class="mark"></div>
    <div class="org-name">Council for Native Elder Wellness</div>
  </div>

  <p class="signs intro" style="top:344px;">Because American Indian and Alaska Native people have a high risk of dementia, it is important to know the warning signs. Do you have any of these 10 signs? If so, talk to your doctor.</p>

  <div class="signs" style="top:417px;">
    <p><span class="lead">1. Memory loss that affects your daily life.</span> <span class="note">You may:</span></p>
    <ul><li>Forget events or important dates</li><li>Repeat yourself</li><li>Rely more often on lists or sticky notes to remember things</li></ul>
  </div>

  <div class="signs" style="top:490px; width:350px;">
    <p><span class="lead">2. Trouble planning or solving problems.</span> <span class="note">You may have a harder time:</span></p>
    <ul><li>Paying bills</li><li>Cooking recipes you have used for years</li></ul>
  </div>

  <div class="signs" style="top:562px;">
    <p class="lead">3. Get confused about the time, date, or where you are.</p>
  </div>

  <div class="signs" style="top:591px;">
    <p class="lead">4. Daily tasks are getting harder, including:</p>
    <ul><li>Driving</li><li>Making a grocery list or going shopping</li></ul>
  </div>

  <div class="signs" style="top:649px; width:500px;">
    <p class="lead">5. Trouble with how your eyesight and thinking work together that gets worse.</p>
    <p class="note">This includes:</p>
    <ul><li>Tripping, falls, or problems with your balance</li><li>Spilling or dropping things more</li></ul>
  </div>

  <div class="signs" style="top:737px; width:470px;">
    <p><span class="lead">6. New trouble talking or writing. You have a hard time finding the words you want to say.</span> <span class="note">For example, you may say “that thing on your wrist that tells time” instead of “watch.”</span></p>
  </div>

  <div class="signs" style="top:795px;">
    <p><span class="lead">7. Lose and cannot find things.</span> <span class="note">For example, you:</span></p>
    <ul><li>Can’t find the coffee pot that you use every day</li><li>Might put your car keys in the freezer</li></ul>
  </div>

  <div class="signs" style="top:853px;">
    <p><span class="lead">8. Notice changes in mood or personality,</span> <span class="note">such as being:</span></p>
    <ul><li>Easily mad or sad in everyday situations</li><li>More fearful (scared) or suspicious (not trusting)</li></ul>
  </div>

  <div class="signs" style="top:911px;">
    <p><span class="lead">9. Act different and make poor choices.</span> <span class="note">This may make you more likely to:</span></p>
    <ul><li>Spend money you do not have or be a scam victim</li><li>Stop washing up regularly or pay less attention to how you look</li><li>Forget to take care of your pet</li></ul>
  </div>

  <div class="signs" style="top:984px; width:490px;">
    <p><span class="lead">10. Pull away from friends and family because it is harder to keep up.</span> <span class="note">You may not want to do things you used to enjoy, like sporting events, church, music or sex.</span></p>
  </div>

  <div class="callout-frame"></div>
  <div class="callout">
    <p class="teal">American Indian and Alaska Native people have a high risk of dementia.</p>
    <p class="mauve">Big changes in memory or thinking that make it hard to get through the day are not a normal part of aging.</p>
    <p class="teal">People with one or more of these 10 signs should talk to their doctor to find the cause. It is not always dementia.</p>
    <p class="mauve">Early dementia diagnosis gives you a chance to get care and plan your future.</p>
  </div>

  <div class="footer-band"></div>
  <div class="partner-card">
    <div class="mark"></div>
    <div class="partner-name">Native Elders Brain Health Resource Hub</div>
  </div>
  <div class="project-card">
    <div class="mark"></div>
    <div class="project-name">Clear Mind Project</div>
  </div>
  <p class="learn-more">To learn more about the warning signs of dementia in American Indian and Alaska Native people, Visit<br>www.NativeElderMind.org<br>www.elderhealthinfo.org/aging</p>
</main>
</body>
</html>
```